Business card design for a debt inventory management software company

We need a business card design to help us move into the next phase of our business. We developed an innovative solution to help companies collect their bad debts. We are moving into a new era and branching out into new industries. We are open to design ideas but would like that they have a similar feel/look to our website and include our logo. https://www.ledgorvia.com

Target Market(s)

Finance Industry, Telecom Industry, Utility Industry, Healthcare Industry, Insurance Industry

Industry/Entity Type

Software

Contact Information for Business Card

Include Name, Title, Phone, Email, website, address, and logo

Font styles to use
Sans Serif

Colors

Designer to choose colors to be used in the design.

Requirements
Must have
• A similar look and feel to our website. https://www.ledgorvia.com

```html
<!DOCTYPE html>
<html lang="en">
<head>
<meta charset="utf-8">
<title>Ledgorvia Software – Business Card</title>
<link href="https://fonts.googleapis.com/css2?family=Montserrat:wght@300&family=Arimo:wght@400;700&display=swap" rel="stylesheet">
<style>
  :root {
    --backdrop: #5a5b5e;
    --card-white: #ffffff;
    --navy: #394264;
    --brand-navy: #2a3370;
    --leaf-green: #7a9a32;
    --text-light: #ffffff;
  }
  html, body {
    margin: 0;
    padding: 0;
    width: 1200px;
    height: 1000px;
    overflow: hidden;
    background: var(--backdrop);
  }
  .canvas {
    position: relative;
    width: 1200px;
    height: 1000px;
  }
  .card {
    position: absolute;
    left: 320px;
    width: 560px;
    height: 320px;
    border-radius: 18px;
    background: var(--card-white);
    overflow: hidden;
    box-shadow: 0 8px 24px rgba(0,0,0,0.35);
  }
  .card--front { top: 130px; }
  .card--back { top: 540px; }

  .wordmark {
    font-family: "Montserrat", sans-serif;
    font-weight: 300;
    color: var(--brand-navy);
    display: flex;
    align-items: center;
    gap: 12px;
    white-space: nowrap;
  }
  .wordmark__square {
    width: 26px;
    height: 26px;
    background: var(--brand-navy);
  }
  .card--front .wordmark {
    position: absolute;
    left: 0; right: 0; top: 0; bottom: 0;
    justify-content: center;
    font-size: 40px;
  }
  .card--back .wordmark {
    position: absolute;
    top: 44px;
    left: 150px;
    font-size: 30px;
  }
  .card--back .wordmark__square { width: 22px; height: 22px; }

  .wave {
    position: absolute;
    left: 0; top: 0;
    width: 560px;
    height: 320px;
  }
  .contact {
    position: absolute;
    font-family: "Arimo", sans-serif;
    color: var(--text-light);
  }
  .contact--person {
    left: 30px;
    top: 134px;
  }
  .person__name {
    font-weight: 700;
    font-size: 21px;
    line-height: 24px;
    letter-spacing: 0.3px;
    margin: 0;
  }
  .person__title {
    font-size: 12px;
    margin: 1px 0 14px;
  }
  .person__address {
    font-size: 12.5px;
    line-height: 15px;
    margin: 0 0 4px;
  }
  .line {
    display: flex;
    align-items: center;
    gap: 7px;
    font-size: 13px;
    line-height: 17px;
  }
  .line svg { width: 12px; height: 12px; flex: none; }
  .contact--web {
    right: 34px;
    bottom: 24px;
  }
  .contact--web .line { font-size: 13.5px; line-height: 20px; }
  .web-strong { font-weight: 700; }
</style>
</head>
<body>
<div class="canvas">

  <section class="card card--front">
    <div class="wordmark"><span class="wordmark__square"></span>Ledgorvia Software</div>
  </section>

  <section class="card card--back">
    <svg class="wave" viewBox="0 0 560 320" preserveAspectRatio="none" aria-hidden="true">
      <path d="M0 98 C150 84 240 128 310 166 C380 204 460 212 560 202 L560 320 L0 320 Z" fill="var(--leaf-green)"/>
      <path d="M0 105 C150 91 240 135 310 173 C380 211 460 219 560 209 L560 320 L0 320 Z" fill="var(--card-white)"/>
      <path d="M0 110 C150 96 240 140 310 178 C380 216 460 224 560 214 L560 320 L0 320 Z" fill="var(--navy)"/>
    </svg>

    <div class="wordmark"><span class="wordmark__square"></span>Ledgorvia Software</div>

    <div class="contact contact--person">
      <p class="person__name">MARTIN HALE</p>
      <p class="person__title">Executive Assistant</p>
      <p class="person__address">240 Harlow Ridge Avenue,<br>Suite 310, Brenton, Ohio 44590</p>
      <div class="line">
        <svg viewBox="0 0 24 24" aria-label="Phone"><path fill="#fff" d="M6.6 10.8a15 15 0 0 0 6.6 6.6l2.2-2.2a1 1 0 0 1 1-.25 11.4 11.4 0 0 0 3.6.57 1 1 0 0 1 1 1V20a1 1 0 0 1-1 1A17 17 0 0 1 3 4a1 1 0 0 1 1-1h3.5a1 1 0 0 1 1 1c0 1.25.2 2.45.57 3.6a1 1 0 0 1-.25 1z"/></svg>
        330.555.0142
      </div>
      <div class="line">
        <svg viewBox="0 0 24 24" aria-label="Fax"><path fill="#fff" d="M6 2h10l2 2v5H6zM3 10h18a1 1 0 0 1 1 1v7h-4v4H6v-4H2v-7a1 1 0 0 1 1-1zm5 7v3h8v-3z"/></svg>
        330.555.0178
      </div>
    </div>

    <div class="contact contact--web">
      <div class="line">
        <svg viewBox="0 0 24 24" aria-label="Email"><path fill="#fff" d="M2 5h20v14H2zm2 2v.5l8 5 8-5V7l-8 5z"/></svg>
        info@ledgorvia.com
      </div>
      <div class="line">
        <svg viewBox="0 0 24 24" aria-label="Website"><circle cx="12" cy="12" r="9" fill="none" stroke="#fff" stroke-width="2"/><path d="M3 12h18M12 3c3 3 3 15 0 18M12 3c-3 3-3 15 0 18" fill="none" stroke="#fff" stroke-width="1.6"/></svg>
        <span>www.<span class="web-strong">ledgorvia</span>.com</span>
      </div>
    </div>
  </section>

</div>
</body>
</html>
```